Business Cards for an 'affordable luxury' inner city home builder in Calgary.

We need a business card design that emulates the progressive, innovative, culture of our company and the modern style of our homes. Use our website www.velmarcrest-ab.com as a reference for the product we build.

Our company builds homes in the inner city space of Calgary, Alberta. We build affordable luxury.

Target Market(s)

Young professional Families

Contact Information for Business Card

Try to maintain consistency with the logo font and the card font.

Requirements
Must have
• The details must include: Name, education, title, phone number, website and email (Address is not as important)
• The design must be uniques (like our logo), elegant, sophisticated and modern.

```html
<!DOCTYPE html>
<html lang="en">
<head>
<meta charset="utf-8">
<title>Velmarcrest Homes Ltd — Business Card</title>
<link rel="stylesheet" href="https://fonts.googleapis.com/css2?family=Open+Sans:wght@400;600&display=swap">
<style>
  :root {
    --paper: #ffffff;
    --ink: #222222;
    --ink-soft: #2b2b2b;
    --band-mid: #808080;
    --band-light: #aaaaab;
    --band-dark: #232323;
    --icon-bg: #9a9a9a;
    --icon-fg: #ffffff;
  }
  html, body {
    margin: 0;
    padding: 0;
    overflow: hidden;
    background: var(--paper);
  }
  .card {
    position: relative;
    width: 1200px;
    height: 686px;
    background: var(--paper);
    overflow: hidden;
    font-family: "Open Sans", Arial, sans-serif;
    color: var(--ink);
  }
  .brand {
    position: absolute;
    left: 122px;
    top: 326px;
    display: flex;
    align-items: center;
    gap: 26px;
  }
  .brand-mark {
    width: 62px;
    height: 62px;
    background: var(--band-mid);
  }
  .brand-name {
    margin: 0;
    font-size: 29px;
    font-weight: 600;
    line-height: 32px;
    letter-spacing: 1.5px;
    color: var(--ink);
  }
  .divider-band {
    position: absolute;
    left: 565px;
    top: 0;
    width: 32px;
    height: 686px;
  }
  .divider-band .seg-mid { fill: var(--band-mid); }
  .divider-band .seg-light { fill: var(--band-light); }
  .divider-band .seg-dark { fill: var(--band-dark); }
  .person {
    position: absolute;
    left: 663px;
    top: 196px;
    width: 372px;
    border-bottom: 2px solid var(--ink);
    padding-bottom: 6px;
  }
  .person-name {
    margin: 0;
    font-size: 46px;
    font-weight: 400;
    line-height: 50px;
    letter-spacing: 0.5px;
  }
  .person-title {
    margin: 0;
    font-size: 25px;
    line-height: 30px;
    letter-spacing: 0.5px;
  }
  .contact-list {
    position: absolute;
    left: 662px;
    top: 302px;
    margin: 0;
    padding: 0;
    list-style: none;
  }
  .contact-item {
    display: flex;
    align-items: center;
    height: 40px;
    margin-bottom: 21.5px;
    font-size: 24px;
    letter-spacing: 0.6px;
    color: var(--ink-soft);
  }
  .contact-icon {
    width: 40px;
    height: 40px;
    margin-right: 17px;
    flex: none;
  }
  .contact-icon .disc { fill: var(--icon-bg); }
  .contact-icon .glyph { fill: var(--icon-fg); }
  .contact-icon .stroke { fill: none; stroke: var(--icon-fg); stroke-width: 1.6; }
</style>
</head>
<body>
<div class="card">
  <div class="brand">
    <div class="brand-mark"></div>
    <p class="brand-name">VELMARCREST<br>HOMES LTD</p>
  </div>

  <svg class="divider-band" viewBox="0 0 32 686" aria-hidden="true">
    <polygon class="seg-mid" points="0,0 32,0 32,166 0,211"/>
    <polygon class="seg-light" points="0,222 32,178 32,424 0,466"/>
    <polygon class="seg-dark" points="0,476 32,434 32,686 0,686"/>
  </svg>

  <div class="person">
    <h1 class="person-name">LOREM IPSUM</h1>
    <p class="person-title">DESIGNATION</p>
  </div>

  <ul class="contact-list">
    <li class="contact-item">
      <svg class="contact-icon" viewBox="0 0 40 40" aria-hidden="true">
        <circle class="disc" cx="20" cy="20" r="20"/>
        <path class="glyph" d="M20 9a7 7 0 0 0-7 7c0 5.5 7 14 7 14s7-8.5 7-14a7 7 0 0 0-7-7zm0 9.6a2.6 2.6 0 1 1 0-5.2 2.6 2.6 0 0 1 0 5.2z"/>
      </svg>
      248 14 Ave NE Calgary, AB
    </li>
    <li class="contact-item">
      <svg class="contact-icon" viewBox="0 0 40 40" aria-hidden="true">
        <circle class="disc" cx="20" cy="20" r="20"/>
        <path class="glyph" d="M14.5 10.5l3 3.6-1.6 2.1c.9 2.2 2.6 3.9 4.8 4.9l2.1-1.6 3.6 3-1.8 3.3c-6.5-.6-12.3-6.4-12.9-12.9z"/>
        <path class="stroke" d="M22 12a6 6 0 0 1 6 6M22 15a3 3 0 0 1 3 3"/>
      </svg>
      403-555-0148
    </li>
    <li class="contact-item">
      <svg class="contact-icon" viewBox="0 0 40 40" aria-hidden="true">
        <circle class="disc" cx="20" cy="20" r="20"/>
        <rect class="glyph" x="10.5" y="13.5" width="19" height="13" rx="1"/>
        <path d="M11 14.5l9 7 9-7" fill="none" stroke="#9a9a9a" stroke-width="1.4"/>
      </svg>
      projects@velmarcrest-ab.com
    </li>
    <li class="contact-item">
      <svg class="contact-icon" viewBox="0 0 40 40" aria-hidden="true">
        <circle class="disc" cx="20" cy="20" r="20"/>
        <circle class="stroke" cx="20" cy="20" r="9"/>
        <ellipse class="stroke" cx="20" cy="20" rx="4" ry="9"/>
        <path class="stroke" d="M11 20h18M12.5 15.5h15M12.5 24.5h15"/>
      </svg>
      www.velmarcrest-ab.com
    </li>
  </ul>
</div>
</body>
</html>
```